we need a business card design for a professional painting business. This company has been up and going for about ten years. However it needs an new logo. we want this business card to be modern eye catching and easy to read. I currently have been looking for VC logos but can not find one that suits our needs. This Design should be Our start to a new beginning.
Industry/Entity Type
Painting
Contact Information for Business Card
Varetti Coatings Inc.
Licensed & Insured
Tomas Varetti
Phone(631)384-4562
Fax (555) 730-2418
E-mail varetticoatingsinc@mailbox.example
Requirements
Must have
- a new logo with  VC and i would like it to be in black and white.
i would also like the front to be a solid black with the logo only and then the back to have the information.

```html
<!DOCTYPE html>
<html lang="en">
<head>
<meta charset="utf-8">
<title>Varetti Coatings Inc. – Business Card</title>
<link rel="stylesheet" href="https://fonts.googleapis.com/css2?family=Pacifico&family=Tinos:ital@1&display=swap">
<style>
  :root {
    --ink: #000000;
    --paper: #ffffff;
    --scribble: #b4b4b4;
    --scribble-dark: #8a8a8a;
    --panel: rgba(40, 40, 40, 0.88);
    --panel-text: #ffffff;
  }
  html, body {
    margin: 0;
    padding: 0;
    overflow: hidden;
  }
  body {
    width: 1034px;
    height: 1200px;
    background: var(--paper);
    position: relative;
  }
  .card {
    position: absolute;
    left: 3px;
    width: 1022px;
    overflow: hidden;
  }
  .card-front {
    top: 3px;
    height: 570px;
    background: var(--ink);
  }
  .logo-disc {
    position: absolute;
    left: 332px;
    top: 104px;
    width: 364px;
    height: 364px;
    border-radius: 50%;
    background: radial-gradient(circle at 45% 40%, #e6e6e6 0%, var(--scribble) 100%);
    display: flex;
    align-items: center;
    justify-content: center;
  }
  .logo-mark {
    font-family: "Pacifico", cursive;
    font-size: 120px;
    color: var(--ink);
    line-height: 1;
  }
  .card-back {
    top: 621px;
    height: 573px;
    background: linear-gradient(160deg, #c8c8c8 0%, var(--scribble) 50%, var(--scribble-dark) 100%);
  }
  .name-panel {
    position: absolute;
    left: 2px;
    top: 34px;
    width: 817px;
    height: 104px;
    border-radius: 22px;
    background: var(--panel);
    display: flex;
    align-items: center;
    padding-left: 24px;
    box-sizing: border-box;
  }
  .company-name {
    margin: 0;
    font-family: "Pacifico", cursive;
    font-weight: 400;
    font-size: 46px;
    color: var(--panel-text);
    letter-spacing: 1px;
    white-space: nowrap;
  }
  .info-panel {
    position: absolute;
    left: 5px;
    top: 256px;
    width: 857px;
    height: 303px;
    border-radius: 34px;
    background: var(--panel);
    padding: 44px 0 0 34px;
    box-sizing: border-box;
  }
  .contact-list {
    margin: 0;
    padding: 0;
    list-style: none;
    font-family: "Tinos", "Times New Roman", serif;
    font-style: italic;
    font-size: 35px;
    line-height: 58.5px;
    color: var(--panel-text);
  }
</style>
</head>
<body>
  <section class="card card-front">
    <div class="logo-disc" role="img" aria-label="Hand-drawn white and grey scribble texture behind the VC monogram">
      <span class="logo-mark">VC</span>
    </div>
  </section>

  <section class="card card-back" role="img" aria-label="Hand-drawn white and grey scribble texture background">
    <div class="name-panel">
      <h1 class="company-name">Varetti Coatings Inc.</h1>
    </div>
    <div class="info-panel">
      <ul class="contact-list">
        <li>Licensed &amp; Insured Tomas Varetti</li>
        <li>Phone(555)217-8093</li>
        <li>Fax (555) 730-2418</li>
        <li>E-mail :varetticoatingsinc@mailbox.example</li>
      </ul>
    </div>
  </section>
</body>
</html>
```